Wordpress design for my private practice website - Psychotherapist

I would like a simple, clean, and elegant design for my private practice website. I work with both adults and children so I'd like it to appeal to both. However, since parents make the choice as to where to send their child for therapy, I want it to appeal to adults more. I would like the pictures on the site to have a calming effect - maybe using sand and water and rocks. I am attaching files with my company logo. I would also like my name incorporated into the header - Colette Brannigan, LCSW, Registered Play Therapist. I've also uploaded a picture of myself for my About Page.

I like the design of these 2 website and want something similar:
www.drlorapenwick.example
www.harwood-tallis.example

I would like a home page that highlights a calming graphic across the entire top of the page as well as my practice logo and my name.

I'd like a link to social media sites on the top of the homepage - facebook, pinterest.

I want a simple bar across the top with the following tabs:
Home
About Me (subtabs Who I Am, Specialties and Approach)
Counseling Services (subtabs Individual Counseling, Play Therapy, Sandplay Therapy,)
Fees
FAQs
Contact Me (would love this to be a fill in the blank contact form that sends info to my email address - should include name, phone number, email and a comment box for more information requested)
Blog (this will link with another wordpress blog)

Target Market(s)

Parents of children under age 12 with behavioral problems or are dealing with the breakup of their family through divorce - looking for someone to work with their young child. I also work with Adults that are overwhelmed and worried - often women that have many life stressors and are feeling burnt out on life and meeting everyone's needs. Families going through some type of trauma, including divorce or grief work. I also work with individuals going through a transition of religious beliefs - often exiting the religion of their youth and undergoing a crisis of faith at midlife.

Industry/Entity Type

Mental Health

Contact Information for Business Card

Colette Brannigan, LCSW
Registered Play Therapist
4917 Wexmoor Lane
Idaho Falls, Idaho 83404
(208)555-0187
www.stillbrookcounseling.example

On the opposite side, I'd like an appointment reminder area - with the following text:

Your next appointment is
_____/______/______ at ______am/pm
Please give 24 hrs notice if you need to cancel your appointment.

Coding

Coded - Design and coding required

Number of Pages Required

5+ page

Font styles to use
Sans Serif

Colors
33a6d7
9bcb3c
0355a3

Requirements
Must have
• I'd like it to be a wordpress site. I'm such a newby at web design - but I need to be able to add content and manage the site myself once it is up and running.
Nice to have
• I like the design of these 2 websites and want something similar:
• www.drlorapenwick.example
• www.harwood-tallis.example
• They are clean, easy to navigate and calming.
Should not have
• Should not look like a childcare website.

```html
<!DOCTYPE html>
<html lang="en">
<head>
<meta charset="utf-8">
<title>Colette Brannigan — Stillbrook Counseling</title>
<link rel="stylesheet" href="https://fonts.googleapis.com/css2?family=Josefin+Sans:wght@300;400&family=Yellowtail&family=Roboto:wght@400;500;700&family=Noticia+Text&display=swap">
<style>
:root{
  --cream:#fdf3e0;
  --sepia:#8a8070;
  --nav:#22527f;
  --page:#f4f4f4;
  --ink:#2a2a2a;
  --sky:#33a6d7;
  --lime:#c6f05a;
  --footer:#7a9325;
  --footer-head:#dcebab;
  --footer-deep:#2c3811;
  --submit:#cfe07c;
  --circle:#2c5f98;
}
*{box-sizing:border-box;margin:0;padding:0}
html,body{width:953px;height:1200px;overflow:hidden}
body{position:relative;background:var(--page);font-family:"Roboto",sans-serif;color:var(--ink)}
.abs{position:absolute}

.hero{left:0;top:0;width:953px;height:350px;
  background:linear-gradient(180deg,var(--cream) 0%,#f3e8d3 25%,#cfc5b3 50%,#8f8676 72%,#4a4238 100%)}
.social-top{top:14px;left:794px;display:flex;gap:7px}
.social-top span{width:23px;height:23px;border-radius:50%;display:block}
.brand{top:68px;left:0;width:953px;text-align:center;color:#5b6470;
  font-family:"Josefin Sans",sans-serif;font-weight:300;font-size:17px;letter-spacing:4px}
.brand-dot{top:24px;left:461px;width:30px;height:30px;border-radius:50%;background:var(--circle)}
.hero-name{top:172px;left:0;width:953px;text-align:center;font-family:"Yellowtail",cursive;
  font-size:52px;color:var(--lime);text-shadow:0 2px 4px rgba(0,0,0,.35)}
.hero-title{top:249px;left:0;width:953px;text-align:center;color:#fff;font-weight:700;font-size:16.5px}

.nav{left:0;top:350px;width:953px;height:38px;background:var(--nav)}
.nav a{position:absolute;top:10px;color:#fff;text-decoration:none;font-family:"Noticia Text",serif;font-size:13px;transform:translateX(-50%);white-space:nowrap}

.welcome-title{top:421px;left:103px;font-family:"Josefin Sans",sans-serif;font-weight:300;font-size:30px;color:#222}
.rule{top:463px;left:105px;width:533px;height:1px;background:#777}
.intro{top:482px;left:105px;width:533px;font-family:"Noticia Text",serif;font-size:9.8px;line-height:13.3px;color:#222}
.intro p{margin-bottom:13px}
.portrait-frame{top:474px;left:670px;width:187px;height:154px;border:1px solid #d8d8d8;background:#fff}
.portrait{top:479px;left:675px;width:178px;height:144px;background:linear-gradient(135deg,#cdb27a,#b89a64 55%,#6e6446)}
.btn{background:var(--sky);color:#fff;font-family:"Noticia Text",serif;text-align:center;border:0}
.read-more{top:649px;left:107px;width:93px;height:32px;line-height:32px;font-size:11.5px}

.help{left:0;top:709px;width:953px;height:343px;background:linear-gradient(90deg,#0b0b09 0%,#12110e 40%,#4a4536 75%,#6c6552 100%)}
.help-title{top:738px;left:0;width:905px;text-align:center;font-family:"Josefin Sans",sans-serif;font-weight:300;font-size:38px;color:var(--lime)}
.help-text{top:792px;left:120px;width:665px;text-align:center;color:#fff;font-size:11.4px;line-height:16px}
.field{background:#fff;border:1px solid #2d7fa8;color:#999;font-size:9.5px;padding:0 9px;display:flex;align-items:center}
.field.area{align-items:flex-start;padding-top:7px}
.send{top:963px;left:386px;width:135px;height:35px;line-height:35px;font-size:11.5px}

.footer{left:0;top:1052px;width:953px;height:113px;background:var(--footer)}
.col-head{top:1071px;font-family:"Noticia Text",serif;font-size:10.5px;color:var(--footer-head)}
.col-list{top:1094px;list-style:none;font-size:8.8px;line-height:16px;color:#fff}
.news-input{top:1094px;left:486px;width:152px;height:23px;background:#fff;color:#999;font-size:8.8px;padding-left:7px;display:flex;align-items:center}
.news-submit{top:1094px;left:638px;width:55px;height:23px;background:var(--submit);font-size:9.5px;text-align:center;line-height:23px;color:#333}
.follow{top:1092px;left:742px;display:flex;gap:11px}
.follow span{width:25px;height:25px;border-radius:50%;background:var(--circle);display:block}
.legal{left:0;top:1165px;width:953px;height:35px;background:var(--footer-deep);color:#fff;font-size:8.8px;text-align:center;line-height:35px;font-weight:500}
.legal em{font-style:normal;color:#d4e57a}
</style>
</head>
<body>

<header>
  <div class="abs hero" role="img" aria-label="Misty sepia seascape with dark rocks rising from calm water"></div>
  <div class="abs social-top">
    <span style="background:#2c5f98" role="img" aria-label="Social profile link"></span>
    <span style="background:#c4302b" role="img" aria-label="Social profile link"></span>
  </div>
  <div class="abs brand-dot"></div>
  <div class="abs brand">STILLBROOK COUNSELING</div>
  <h1 class="abs hero-name">Colette Brannigan</h1>
  <div class="abs hero-title">LCSW, REGISTERED PLAY THERAPIST</div>
</header>

<nav class="abs nav">
  <a style="left:203px">Home</a>
  <a style="left:301px">About Me</a>
  <a style="left:437px">Counseling Services</a>
  <a style="left:559px">Fees</a>
  <a style="left:640px">FAQs</a>
  <a style="left:739px">Contact Me</a>
</nav>

<main>
  <h2 class="abs welcome-title">Colette Brannigan Welcomes You</h2>
  <div class="abs rule"></div>
  <div class="abs intro">
    <p>Duis gravida rhoncus enim vitae porttitor. Vivamus eget massa venenatis, aliquet mi vel, pellentesque ligula. Fusce sed massa sed orci condimentum efficitur in sit amet orci. Duis condimentum dolor eu sapien tempus dignissim. Nam elementum urna et erat luctus aliquam. Phasellus ut fringilla arcu, et dignissim lacus. Nulla facilisi. Mauris id nisi purus.</p>
    <p>Morbi ultrices tincidunt mauris in cursus. Phasellus vitae posuere justo. Nulla interdum elit quis nulla bibendum, at vulputate magna faucibus. Mauris tristique, nisi nec rutrum aliquet, nisl urna dignissim orci, ut cursus urna neque eu dolor.</p>
    <p>Aliquam quis elit risus. Donec finibus nisl sit amet finibus pulvinar. Nulla dignissim, neque ac tincidunt imperdiet, leo libero pellentesque leo, quis porta augue purus eget nunc. Cras vitae massa massa. Donec ultrices, turpis sit amet blandit ultrices, lectus metus lobortis mi, eget sodales lorem massa finibus dolor.</p>
  </div>
  <div class="abs portrait-frame"></div>
  <div class="abs portrait" role="img" aria-label="Portrait photograph of the therapist outdoors in golden grass"></div>
  <div class="abs btn read-more">Read More</div>

  <section>
    <div class="abs help" role="img" aria-label="Dark photograph of smooth river stones in flowing water"></div>
    <h2 class="abs help-title">I’m Here To Help You.</h2>
    <p class="abs help-text">If you have any&nbsp; queries on online presence and online store management and other web related things please send us mail with a brief of your question.</p>
    <div class="abs field" style="top:864px;left:183px;width:260px;height:29px">Your Name</div>
    <div class="abs field" style="top:905px;left:183px;width:260px;height:28px">Your Email id</div>
    <div class="abs field area" style="top:864px;left:466px;width:259px;height:69px">Your Queries</div>
    <div class="abs btn send">Send</div>
  </section>
</main>

<footer>
  <div class="abs footer"></div>
  <div class="abs col-head" style="left:96px">About</div>
  <ul class="abs col-list" style="left:96px"><li>Who I Am</li><li>Specialties</li><li>Approach</li></ul>
  <div class="abs col-head" style="left:188px">Counselling Services</div>
  <ul class="abs col-list" style="left:188px"><li>Individual Counseling</li><li>Play Therapy</li><li>Sandplay Therap</li></ul>
  <div class="abs col-head" style="left:335px">Latest Posts</div>
  <ul class="abs col-list" style="left:335px"><li>Lorem ipsumm dolor sit</li><li>Nuno valencia esdt di</li><li>Di maria nuno estelem</li></ul>
  <div class="abs col-head" style="left:483px">Subscribe Newsletter</div>
  <div class="abs news-input">Your Email id</div>
  <div class="abs news-submit">Submit</div>
  <div class="abs col-head" style="left:742px">Follow Me</div>
  <div class="abs follow">
    <span role="img" aria-label="Social profile link"></span>
    <span style="background:#2f8ad0" role="img" aria-label="Social profile link"></span>
    <span style="background:#c4302b" role="img" aria-label="Social profile link"></span>
  </div>
  <div class="abs legal">Colette Brannigan© 2016 Copyright&nbsp; <em>|&nbsp; Make an enquiry&nbsp; |&nbsp; Privacy statement.</em></div>
</footer>

</body>
</html>
```